Marketing & Media Production Company wants edgy DESIGN + CODING

Please find enclosed in the Brief document
we really want this website to be edgy, monochrome (ie. only two colors - white + black) with some nice background imagery STRICTLY based on the logo.
The logo is a sumerian eagle, it would be great to keep this as a subtle background theme but dont go crazy on this.
Please feel free to ignore the layout in the document if you think you can come up with one that is better, ideally we want the layout to be CLEAR and easy to decipher - with a really good contact form on the front page.
We want the website to be cool, funky, so if you want to have a introductory picture that must be clicked (logo) or something like that (eg this website:
Please NOTE:
Page Structure is as follows:
1 ABOUT US > (subpage) Meet the Team
2 CLIENTS > (subpage) Case Studies
3 SERVICES > (subpage) Portfolio
4 CONTACT

```html
<!DOCTYPE html>
<html lang="en">
<head>
<meta charset="UTF-8">
<title>Vantage — Digital Marketing &amp; Media Production</title>
<link href="https://fonts.googleapis.com/css2?family=Raleway:wght@300;400;500;600;700;800&family=Open+Sans:wght@400;600&display=swap" rel="stylesheet">
<style>
:root{
  --ink:#111111;
  --ink-soft:#333333;
  --grey:#777777;
  --grey-light:#bdbdbd;
  --text-muted:#8a8a8a;
  --paper:#ffffff;
  --hero-top:#ffffff;
  --hero-bottom:#ececec;
  --band:#2e2e2e;
  --field:#2a2a2a;
  --field-line:#4a4a4a;
}
*{box-sizing:border-box;margin:0;padding:0}
html,body{width:914px;height:1200px;overflow:hidden;background:var(--paper)}
body{position:relative;font-family:'Open Sans',sans-serif;color:var(--ink)}
a{color:inherit;text-decoration:none}

.site-header{position:absolute;left:0;top:0;width:914px;height:130px}
.main-nav a{position:absolute;top:57px;font-family:'Raleway',sans-serif;font-weight:500;font-size:14.5px;letter-spacing:.2px;color:var(--ink)}
.brand{position:absolute;left:358px;top:14px;width:200px;text-align:center}
.brand-dot{display:block;width:40px;height:40px;border-radius:50%;background:var(--ink);margin:0 auto 24px}
.brand-name{font-family:'Raleway',sans-serif;font-weight:600;font-size:15px;letter-spacing:8px;color:var(--ink);padding-left:8px}

.hero{position:absolute;left:0;top:130px;width:914px;height:373px;background:linear-gradient(var(--hero-top) 30%,var(--hero-bottom));border-bottom:1px solid #e0e0e0}
.hero-kicker{position:absolute;left:102px;top:85px;font-family:'Raleway',sans-serif;font-weight:700;font-size:22px;color:var(--grey)}
.hero-title{position:absolute;left:102px;top:113px;font-family:'Raleway',sans-serif;font-weight:800;font-size:31px;color:var(--ink)}
.hero-copy{position:absolute;left:103px;top:157px;width:350px;font-size:7.8px;line-height:13.5px;color:#666}
.btn-more{position:absolute;left:103px;top:205px;width:83px;height:25px;border-radius:3px;background:linear-gradient(#4a4a4a,#1e1e1e);color:#fff;font-size:9.5px;font-weight:600;line-height:25px;text-align:center}
.slider-dots{position:absolute;left:104px;top:243px;display:flex;gap:2px}
.slider-dots span{width:10px;height:10px;border-radius:50%;background:var(--grey-light)}
.slider-dots span.active{background:var(--ink)}
.hero-visual{position:absolute;left:525px;top:20px;width:215px;height:318px;border-radius:6px;background:radial-gradient(ellipse at 50% 40%,#9a9a9a,#d8d8d8 70%,rgba(236,236,236,0))}

.section-title{font-family:'Raleway',sans-serif;font-weight:400;font-size:19px;color:var(--ink-soft)}
.services{position:absolute;left:101px;top:530px;width:350px}
.services .section-title{margin-left:2px}
.service{position:absolute;left:0;width:350px}
.service-icon{position:absolute;left:0;top:0;width:58px;height:58px;border-radius:50%;background:var(--ink)}
.service-icon svg{position:absolute;left:14px;top:14px;width:30px;height:30px}
.item-body{position:absolute;left:69px;top:2px;width:275px}
.item-title{font-family:'Raleway',sans-serif;font-weight:400;font-size:12.5px;color:var(--ink-soft);margin-bottom:3px}
.item-text{font-size:7.5px;line-height:12.3px;color:var(--text-muted)}
.read-link{display:block;margin-top:2px;font-size:7.8px;font-weight:600;color:var(--ink)}

.news{position:absolute;left:484px;top:532px;width:330px}
.news-item{position:absolute;left:1px;width:325px}
.news-item .item-title{font-size:11px}

.contact-band{position:absolute;left:0;top:848px;width:914px;height:241px;background:var(--band)}
.contact-title{position:absolute;left:0;top:34px;width:914px;text-align:center;font-family:'Raleway',sans-serif;font-weight:400;font-size:23px;color:#fff}
.field{position:absolute;background:var(--field);border:1px solid var(--field-line);border-radius:3px;color:#cfcfcf;font-size:8px;padding:0 9px;line-height:22px}
.field-message{line-height:1;padding-top:9px}
.btn-submit{position:absolute;left:241px;top:161px;width:424px;height:27px;border-radius:2px;background:linear-gradient(#ffffff,#e2e2e2);font-family:'Raleway',sans-serif;font-weight:500;font-size:11.5px;color:var(--ink);line-height:27px;text-align:center}

.site-footer{position:absolute;left:0;top:1089px;width:914px;height:111px;text-align:center}
.footer-nav{margin-top:23px;font-family:'Raleway',sans-serif;font-weight:500;font-size:12px;color:var(--ink-soft);word-spacing:2px}
.footer-nav .sep{margin:0 10px}
.copyright{margin-top:8px;font-size:7.5px;color:#555}
.social{margin-top:13px;display:flex;justify-content:center;gap:10px}
.social span{width:14px;height:14px;border-radius:50%;background:#444}
</style>
</head>
<body>

<header class="site-header">
  <nav class="main-nav">
    <a href="#" style="left:134px">ABOUT US</a>
    <a href="#" style="left:258px">CLIENTS</a>
    <a href="#" style="left:579px">SERVICES</a>
    <a href="#" style="left:698px">CONTACT US</a>
  </nav>
  <div class="brand">
    <span class="brand-dot"></span>
    <div class="brand-name">VANTAGE</div>
  </div>
</header>

<section class="hero">
  <p class="hero-kicker">DIGITAL MARKETING &amp;</p>
  <h1 class="hero-title">MEDIA PRODUCTION</h1>
  <p class="hero-copy">Morbi diam mauris viverra in gravida eu mattis in ante Morbi eget arcu Morbi porta libero id ullamcorper nonummy nibh ligula pulvinar metus eget consectetuer augue nisi quis lacus Ut ac mi quis lacus mollis aliquam Curabitur iaculis tempus eros Curabitur vel</p>
  <a class="btn-more" href="#">READ MORE</a>
  <div class="slider-dots"><span class="active"></span><span></span><span></span><span></span></div>
  <div class="hero-visual" role="img" aria-label="Professional film camera mounted on a tripod"></div>
</section>

<section class="services">
  <h2 class="section-title">Our Services</h2>
  <article class="service" style="top:44px">
    <div class="service-icon">
      <svg viewBox="0 0 30 30"><path d="M22 6 C15 7 11 12 9 17 L13 21 C18 19 23 15 24 8 Z" fill="#fff"/><path d="M9 17 L5 18 L8 14 Z M13 21 L12 25 L16 22 Z M8 20 L6 25 L11 23 Z" fill="#fff"/></svg>
    </div>
    <div class="item-body">
      <h3 class="item-title">Digital Marketing</h3>
      <p class="item-text">Morbi ornare gravida elit Integer congue augue et malesuada iaculis ipsum dui aliquet felis at cursus magna nisl nec elit Praesent elementum</p>
      <a class="read-link" href="#">Read More</a>
    </div>
  </article>
  <article class="service" style="top:123px">
    <div class="service-icon">
      <svg viewBox="0 0 30 30"><rect x="4" y="9" width="16" height="13" rx="2" fill="#fff"/><path d="M20 14 L27 10 L27 21 L20 17 Z" fill="#fff"/></svg>
    </div>
    <div class="item-body">
      <h3 class="item-title">Media Productions</h3>
      <p class="item-text">Morbi ornare gravida elit Integer congue augue et malesuada iaculis ipsum dui aliquet felis at cursus magna nisl nec elit Praesent ele</p>
      <a class="read-link" href="#">Read More</a>
    </div>
  </article>
  <article class="service" style="top:202px">
    <div class="service-icon">
      <svg viewBox="0 0 30 30"><g fill="#fff"><circle cx="11" cy="13" r="6"/><circle cx="21" cy="20" r="4"/><circle cx="21" cy="9" r="3"/></g><g fill="#000"><circle cx="11" cy="13" r="2"/><circle cx="21" cy="20" r="1.4"/><circle cx="21" cy="9" r="1"/></g></svg>
    </div>
    <div class="item-body">
      <h3 class="item-title">Training Service</h3>
      <p class="item-text">Morbi ornare gravida elit Integer congue augue et malesuada iaculis ipsum dui aliquet felis at cursus magna nisl nec elit Praesent elementum</p>
      <a class="read-link" href="#">Read More</a>
    </div>
  </article>
</section>

<section class="news">
  <h2 class="section-title">Latest News</h2>
  <article class="news-item" style="top:36px">
    <h3 class="item-title">Morbi diam mauris viverra in gravida</h3>
    <p class="item-text">Ut ac mi quis lacus mollis aliquam Curabitur iaculis tempus eros Curabitur vel mi sit amet magna malesuada ultrices Ut nisi erat fermentum vel congue id euismod in elit Fusce ultricies orci ac feugiat suscipit leo massa</p>
    <a class="read-link" href="#">Read More</a>
  </article>
  <article class="news-item" style="top:126px">
    <h3 class="item-title">Proin nulla arcu nonummy luctus dictum</h3>
    <p class="item-text">Ut ac mi quis lacus mollis aliquam Curabitur iaculis tempus eros Curabitur vel mi sit amet magna malesuada ultrices Ut nisi erat fermentum vel congue id euismod in e</p>
    <a class="read-link" href="#">Read More</a>
  </article>
  <article class="news-item" style="top:204px">
    <h3 class="item-title">Nunc porta convallis pede</h3>
    <p class="item-text">Ut ac mi quis lacus mollis aliquam Curabitur iaculis tempus eros Curabitur vel mi sit amet magna malesuada ultrices Ut nisi erat fermentum vel congue id euismod in e</p>
    <a class="read-link" href="#">Read More</a>
  </article>
</section>

<section class="contact-band">
  <h2 class="contact-title">CONTACT FORM</h2>
  <div class="field" style="left:242px;top:77px;width:208px;height:23px">Your Name</div>
  <div class="field" style="left:242px;top:105px;width:208px;height:23px">Email address</div>
  <div class="field" style="left:242px;top:132px;width:208px;height:23px">Phone no.</div>
  <div class="field field-message" style="left:457px;top:77px;width:208px;height:78px">Message</div>
  <a class="btn-submit" href="#">Submit Now</a>
</section>

<footer class="site-footer">
  <nav class="footer-nav">
    <a href="#">HOME</a><span class="sep">|</span><a href="#">ABOUT US</a><span class="sep">|</span><a href="#">CLIENTS</a><span class="sep">|</span><a href="#">SERVICES</a><span class="sep">|</span><a href="#">CONTACT</a>
  </nav>
  <p class="copyright">© 2014 Company Name &nbsp;All right reserved &nbsp;Term of Use</p>
  <div class="social" aria-label="Social links"><span></span><span></span><span></span></div>
</footer>

</body>
</html>
```